Outpost Lattice Advisors – Franchise Growth & Development Presentation

Outpost Lattice Advisors is an outsourced franchise sales organization (FSO) that helps franchisors grow their franchise systems without the expense and risk of hiring an internal franchise development team.

We are seeking a professional PowerPoint presentation that will be used to present our services to franchisors, franchise executives, founders, and growth-stage franchise brands.

The presentation should communicate the value of partnering with Outpost Lattice Advisors, including:

• Fractional franchise sales team versus hiring internal staff
• 30+ years of franchise industry experience
• 550+ franchise sales successes
• Immediate access to established franchise broker relationships
• Proven franchise development processes
• Franchise growth strategy and enterprise value creation
• Potential private equity and exit opportunities through franchise expansion

The presentation should feel like a modern consulting, investment, or growth strategy presentation rather than a typical sales brochure. We want strong visual storytelling, custom infographics, professional diagrams, and clean business-oriented design.

The audience includes business owners, franchise founders, franchise executives, and investors who are evaluating growth strategies for their franchise systems.

Target Market(s)

Primary Audience: Emerging franchisors Growth-stage franchise brands Franchise founders Franchise CEOs Franchise presidents Franchise development executives Secondary Audience: Private equity firms Franchise investors Strategic buyers Franchise consultants

Industry/Entity Type

Franchise Development, Private Equity / Business Expansion

Font styles to use
Other font styles liked:
• Use Montserrat for titles and Open Sans for body text.

Requirements
Must have
• Modern professional business design Consistent branding throughout Custom infographics Comparison graphics Broker network ecosystem graphic Enterprise value graphic Easy-to-read charts and visuals Editable PowerPoint format Professional iconography. www.outpostlatticeadvisors.example as reference for colors
Nice to have
• Franchise-related imagery Subtle growth-themed visuals Timeline graphics Data visualization Private equity / valuation style graphics
Should not have
• Cartoon graphics Clip art Overly busy slides Stock-template appearance Bright neon colors Handwritten fonts Excessive text on slides Juvenile or playful design elements

```html
<!DOCTYPE html>
<html lang="en">
<head>
<meta charset="utf-8">
<title>Why Outpost Lattice Advisors Is Different</title>
<link rel="stylesheet" href="https://fonts.googleapis.com/css2?family=Montserrat:wght@800&family=Inter:wght@500&display=swap">
<style>
  :root {
    --navy-deep: #0f2d4f;
    --navy: #17395f;
    --orange: #fb9b05;
    --white: #ffffff;
    --pill-light: #f5f5f7;
    --ink: #123354;
  }
  * { margin: 0; padding: 0; box-sizing: border-box; }
  html, body { width: 1200px; height: 675px; overflow: hidden; }
  body { background: var(--navy-deep); }
  .slide {
    position: relative;
    width: 1200px;
    height: 675px;
    overflow: hidden;
  }
  .backdrop {
    position: absolute;
    inset: 0;
    background:
      radial-gradient(ellipse at 70% 40%, rgba(60,95,135,0.45), transparent 60%),
      linear-gradient(180deg, #1a3d63 0%, #163659 45%, #0f2b4c 100%);
  }
  .title {
    position: absolute;
    top: 40px;
    left: 0;
    width: 1200px;
    text-align: center;
    font-family: "Montserrat", sans-serif;
    font-weight: 800;
    font-size: 33px;
    line-height: 36px;
    color: var(--white);
    letter-spacing: 0.3px;
  }
  .title .accent { color: var(--orange); }
  .pill {
    position: absolute;
    height: 38px;
    border-radius: 7px;
    display: flex;
    align-items: center;
    justify-content: center;
    font-family: "Inter", sans-serif;
    font-weight: 500;
    font-size: 17.5px;
    color: var(--ink);
    background: var(--pill-light);
  }
  .pill.highlight { background: var(--orange); }
</style>
</head>
<body>
<div class="slide">
  <div class="backdrop" role="img" aria-label="Dimmed navy-toned photo of executives in a boardroom meeting with a presenter and growth charts"></div>
  <h1 class="title">WHY OUTPOST <span class="accent">LATTICE</span><br><span class="accent">ADVISORS</span> IS DIFFERENT?</h1>

  <div class="pill" style="left:178px; top:229px; width:252px;">Fractional cost model</div>
  <div class="pill highlight" style="left:474px; top:229px; width:252px;">Immediate execution</div>
  <div class="pill" style="left:770px; top:229px; width:252px;">550+ franchise sales</div>

  <div class="pill" style="left:110px; top:337px; width:252px;">30+ years’ experience</div>
  <div class="pill highlight" style="left:408px; top:337px; width:296px;">Established broker network</div>
  <div class="pill" style="left:750px; top:337px; width:340px;">Proven franchise growth systems</div>

  <div class="pill highlight" style="left:465px; top:445px; width:270px;">Strategic growth partner</div>
</div>
</body>
</html>
```